Halloway Hall for the Arts Event Listing Template for Newsprint and Social Media

We are an event venue and would like a template made for a newspaper ad...no bigger than 3x5 that we can list the acts/artists that will be performing each month. We use art nouveau stylings and live in a small mountain town. Ideally it would be something that we could change from month to month, listing the calendar of events each month. Im envisioning somwehing with a decorative border so the public recognizes it each month. Black and white. Classic. Room for 4-6 artists and also room to have 2-3 months listed at a time if we only have 2 acts a month.<br/>It would need to have our address, website and Adv tix available on Ticketplume.com. The poster we ahve is too busy for a newspaper. Just seeking a border template that we could input the names/info of thee concerts/events each month.

Target Market(s)

Our community and surrounding areas. Art and music lovers. All ages

Industry/Entity Type

Entertainment Industry

Font styles to use
Other font styles liked:
• ill send font examples...also see our website at www.hallowayhallforthearts.com

Colors
3176b5
876aae
b868aa
00a990
33a6d7

Requirements
Must have
• Style. Clarity. Artistic flair. Timeless. Ease of adaptability. Unique branding aka our website www.hallowayhallforthearts.com, our name, address, website and place to add artists/events each month, suitability for newsprint and social media
Nice to have
• beauty, artistic interest, unique style, black and white and color options, perhaps a art nouveau border using our logo, flowers, woman
Should not have
• helvetica or other boring font, pop art, neon colors. music notes or any other art/music graphics, illegible text

```html
<!DOCTYPE html>
<html lang="en">
<head>
<meta charset="utf-8">
<title>Halloway Hall for the Arts – Upcoming Shows February 2020</title>
<link href="https://fonts.googleapis.com/css2?family=Poiret+One&family=Righteous&family=Lato:wght@400&display=swap" rel="stylesheet">
<style>
  :root {
    --paper: #ffffff;
    --ink: #111111;
    --ink-soft: #333333;
    --grey-light: #d6d6d6;
    --grey-mid: #9a9a9a;
    --grey-dark: #555555;
  }
  * { box-sizing: border-box; margin: 0; padding: 0; }
  html, body { width: 720px; height: 1200px; overflow: hidden; background: var(--paper); }
  .poster {
    position: relative; width: 720px; height: 1200px; overflow: hidden;
    background: var(--paper); color: var(--ink);
    font-family: "Lato", Arial, sans-serif;
  }
  .border-frame { position: absolute; inset: 0; width: 720px; height: 1200px; }

  .masthead {
    position: absolute; left: 22px; top: 22px; width: 426px; height: 255px;
    background: var(--ink); border-bottom-right-radius: 56px;
    text-align: center; color: var(--paper);
  }
  .masthead .rule { position: absolute; left: 22px; right: 22px; height: 1px; background: var(--paper); }
  .masthead .rule.top { top: 72px; }
  .masthead .rule.bottom { top: 122px; }
  .venue-mark {
    position: absolute; left: 201px; top: 36px; width: 24px; height: 24px;
    border: 2px solid var(--paper); border-radius: 50%;
  }
  .venue-name {
    position: absolute; left: 0; right: 0; top: 84px;
    font-family: "Poiret One", sans-serif; font-size: 23px; letter-spacing: 1px; line-height: 28px;
  }
  .headline {
    position: absolute; left: 0; right: 0; top: 152px;
    font-family: "Poiret One", sans-serif; font-weight: 400;
    font-size: 37px; line-height: 44px; letter-spacing: 2px;
  }

  .show { position: absolute; left: 27px; width: 670px; height: 100px; }
  .show .thumb {
    position: absolute; left: 0; top: 0; width: 95px; height: 94px;
    border: 4px solid var(--ink);
    background: linear-gradient(135deg, var(--grey-light), var(--grey-dark));
  }
  .show .details {
    position: absolute; left: 136px; top: 0; width: 422px; min-height: 94px;
    background: var(--paper); border: 1px solid var(--ink); border-radius: 8px; padding: 7px 14px 8px;
  }
  .show h2 {
    font-family: "Poiret One", sans-serif; font-weight: 400; color: var(--ink);
    font-size: 22px; letter-spacing: 1px; line-height: 24px; margin-bottom: 2px;
  }
  .show p { font-size: 11.5px; line-height: 14.5px; letter-spacing: .6px; color: var(--ink-soft); }
  .show .date {
    position: absolute; left: 568px; top: -3px; width: 100px; height: 100px;
    border-radius: 50%; background: var(--ink); border: 3px solid var(--paper);
    box-shadow: 0 0 0 1.5px var(--ink);
    text-align: center; padding-top: 22px; color: var(--paper);
  }
  .date .day { display: block; font-family: "Righteous", sans-serif; font-size: 15px; line-height: 18px; letter-spacing: .5px; }
  .date .num { display: block; font-family: "Righteous", sans-serif; font-size: 27px; line-height: 32px; }

  .footer-rules { position: absolute; left: 36px; right: 36px; top: 1118px; height: 10px; }
  .footer-rules .line-dots { position: absolute; left: 0; right: 0; top: 2px; border-top: 2px dotted var(--ink); }
  .footer-rules .line-solid { position: absolute; left: 0; right: 0; top: 8px; height: 1px; background: var(--ink); }
  .contact {
    position: absolute; left: 0; right: 0; top: 1138px; text-align: center;
    color: var(--ink); font-size: 12px; line-height: 16px; letter-spacing: 1px;
  }
</style>
</head>
<body>
<main class="poster">
  <svg class="border-frame" viewBox="0 0 720 1200" aria-hidden="true">
    <g fill="none" stroke="#111111">
      <rect x="8" y="8" width="704" height="1184" stroke-width="2.5"/>
      <rect x="15" y="15" width="690" height="1170" stroke-width="0.8"/>
      <path d="M8 44 A36 36 0 0 0 44 8" stroke-width="1"/>
      <path d="M676 8 A36 36 0 0 0 712 44" stroke-width="1"/>
      <path d="M712 1156 A36 36 0 0 0 676 1192" stroke-width="1"/>
      <path d="M44 1192 A36 36 0 0 0 8 1156" stroke-width="1"/>
      <circle cx="8" cy="8" r="5" fill="#111111"/>
      <circle cx="712" cy="8" r="5" fill="#111111"/>
      <circle cx="712" cy="1192" r="5" fill="#111111"/>
      <circle cx="8" cy="1192" r="5" fill="#111111"/>
    </g>
  </svg>

  <header class="masthead">
    <span class="venue-mark"></span>
    <span class="rule top"></span>
    <div class="venue-name">HALLOWAY HALL FOR THE ARTS</div>
    <span class="rule bottom"></span>
    <h1 class="headline">UPCOMING SHOWS<br>FEBRUARY 2020</h1>
  </header>

  <section class="show" style="top:320px">
    <div class="thumb" role="img" aria-label="Photo of a fiddler in a black hat"></div>
    <div class="details">
      <h2>WREN CALLOWAY</h2>
      <p>Award winning fiddler mixes. Appalachian-style with Texas twang, Indian ragas &amp; gypsy jazz. Rare solo performance! $15 adv $20 at the door. 7pm Special Valentines for All</p>
    </div>
    <div class="date"><span class="day">FRIDAY</span><span class="num">7/02</span></div>
  </section>

  <section class="show" style="top:462px">
    <div class="thumb" role="img" aria-label="Photo of a musician in a cowboy hat on stage"></div>
    <div class="details">
      <h2>SONG-ETRY</h2>
      <p>Songwriting Workshop with master musician Eli Marston. Everyone will leave with a song...your 1st or your 50th!<br>$35 =2 for 1 shoe tixs<br>Space is limited. 2-4pm</p>
    </div>
    <div class="date"><span class="day">SUNDAY</span><span class="num">9/02</span></div>
  </section>

  <section class="show" style="top:614px">
    <div class="thumb" role="img" aria-label="Photo of a father and daughter musical duo"></div>
    <div class="details">
      <h2>JUNE &amp; ELI MARSTON</h2>
      <p>This father daughter duo has performed together all over the world to standing ovations. With crazy instruments and great musical prowess.<br>$15 adv $20 at the door 6 pm.</p>
    </div>
    <div class="date"><span class="day">TUESDAY</span><span class="num">10/02</span></div>
  </section>

  <section class="show" style="top:772px">
    <div class="thumb" role="img" aria-label="Photo of a singer playing accordion"></div>
    <div class="details">
      <h2>TOBIAS VELLAN</h2>
      <p>THE KESTRELS lead singer and accordianist brings an unforgettable night of Yiddish music with Latvian Singer Ilze Varna and European violinist Niko Brandt<br>$20 adv $25 at the door, 7 pm</p>
    </div>
    <div class="date"><span class="day">SUNDAY</span><span class="num">16/02</span></div>
  </section>

  <section class="show" style="top:938px">
    <div class="thumb" role="img" aria-label="Photo of a four-piece bluegrass band with instruments"></div>
    <div class="details">
      <h2>THE TIMBERLINE ACCORD</h2>
      <p>Nominated for a Harmonia Award in 2017 The Timberline Accord has been thrilling their Bluegrass loving audiences for decades.<br>$15 adv $20 at the door. 7pm</p>
    </div>
    <div class="date"><span class="day">FRIDAY</span><span class="num">21/02</span></div>
  </section>

  <div class="footer-rules"><span class="line-dots"></span><span class="line-solid"></span></div>

  <footer class="contact">
    www.hallowayhallforthearts.com<br>
    418 Cedar Ridge, Alder Falls Adv Tix avail at Ticketplume.com
  </footer>
</main>
</body>
</html>
```